依頼詳細
グランドオープンに合わせて4日間限定の来店者プレゼント企画を開催します。その告知として、新聞折り込みにチラシを入れようと思うます。今回はその、折り込み用チラシの作成をお願いいたします。プレゼント内容は5/29,30,31,6/1「プチシュープレゼント」各日50名限定となります。
記載項目
「グランドオープン」であること、「5/29,30、31,6/1各日 50名様限定スイーツプレゼント」があること(プレゼント内容の記載はしても、しなくてもどちらでもokです。)、店名ロゴ(添付)、〒371-0815 群馬県沼田市栄和町2871-5 TEL&FAX 0278-61-7350 FaceBookページ有♪
サイズ
B5
ページ数
片面
希望イメージ
シンプル 複雑
単色 カラフル
暗い 明るい
日常 高級
遊び心 厳粛
未来的 伝統的
女性的 男性的
希望する色
緑 青
納品ファイル
• 高解像度JPG (.jpg)
補足説明
プレゼント内容の変更。
5/29,30 プチシュー 各日限定50個
5/31,6/1 いちごミルクプリン 各日限定50個 となります。
ロゴファイル追加です

自店のcolorにとてもあっていたから
シンプルなのにインパクトが大きく目を引く配色だったため

色々なデザインを頂きありがとうございました。自分ではなかなか出てこない案が多くロゴの時も感じましたが、とてもいい刺激になりました。
ありがとうございました。

```html
<!DOCTYPE html>
<html lang="ja">
<head>
<meta charset="utf-8">
<title>Sweets&amp;Cafe こもれび グランドオープン</title>
<link href="https://fonts.googleapis.com/css2?family=M+PLUS+Rounded+1c:wght@500;700;800&family=Pacifico&display=swap" rel="stylesheet">
<style>
  :root{
    --green:#7cc242;
    --green-deep:#4e9a2a;
    --green-pale:#e9f5d8;
    --leaf-light:#b9de8a;
    --blue:#1f4f9f;
    --blue-deep:#163b7a;
    --pink:#e2337d;
    --paper:#ffffff;
    --ink:#333333;
  }
  *{margin:0;padding:0;box-sizing:border-box}
  html,body{width:885px;height:1200px;overflow:hidden;background:var(--paper)}
  body{font-family:"M PLUS Rounded 1c",sans-serif;color:var(--ink)}
  .flyer{position:relative;width:885px;height:1200px;background:var(--paper);overflow:hidden}
  .pattern-top{position:absolute;left:0;top:0;width:885px;height:70px;
    background:linear-gradient(180deg,var(--green-pale),rgba(233,245,216,0))}
  .tagline{position:absolute;top:38px;width:100%;text-align:center;font-size:21px;font-weight:700;color:var(--green-deep);letter-spacing:1px}
  .brand{position:absolute;top:105px;width:100%;text-align:center;color:var(--green);font-weight:800;line-height:1}
  .brand .small{display:block;font-size:46px}
  .brand .large{display:block;font-size:92px;margin-top:8px}
  .ribbon{position:absolute;left:0;top:272px;width:885px;height:180px}
  .ribbon-title{position:absolute;left:150px;top:286px;font-family:"Pacifico",cursive;font-size:80px;color:var(--paper);line-height:1.2}
  .ribbon-date{position:absolute;left:688px;top:340px;font-family:"Pacifico",cursive;font-size:42px;line-height:1.2;color:var(--blue);transform:rotate(-8deg)}
  .side-leaf{position:absolute;top:470px;width:70px;height:70px;border-radius:50%;background:var(--leaf-light)}
  .side-leaf.left{left:60px}
  .side-leaf.right{left:755px}
  .lead{position:absolute;top:468px;width:100%;text-align:center;color:var(--green-deep);font-weight:800}
  .lead .line1{display:block;font-size:30px}
  .lead .line2{display:block;font-size:40px;margin-top:6px}
  .offer{position:absolute;top:590px;width:335px}
  .offer.left{left:32px}
  .offer.right{left:518px}
  .offer-date{background:var(--green);color:var(--pink);font-weight:800;font-size:30px;text-align:center;padding:6px 0;border-radius:4px}
  .offer-date .dow{font-size:20px}
  .offer-box{margin-top:8px;border:2px solid var(--green);height:74px;display:flex;align-items:center;justify-content:center;color:var(--pink);font-weight:700;font-size:30px}
  .limit-badge{position:absolute;left:382px;top:590px;width:122px;height:122px;border-radius:50%;background:var(--blue);color:var(--paper);text-align:center;font-weight:800;display:flex;flex-direction:column;justify-content:center;line-height:1.15}
  .limit-badge .s{font-size:20px}
  .limit-badge .n{font-size:34px}
  .limit-badge .n small{font-size:18px}
  .pattern-bottom{position:absolute;left:0;top:752px;width:885px;height:78px;
    background:linear-gradient(0deg,var(--green-pale),rgba(233,245,216,0.35))}
  .footer{position:absolute;left:0;top:830px;width:885px;height:370px;background:var(--green)}
  .footer-brand{position:absolute;left:40px;top:34px;color:var(--paper);font-weight:800;line-height:1}
  .footer-brand .small{display:block;font-size:26px}
  .footer-brand .large{display:block;font-size:50px;margin-top:6px}
  .hours{position:absolute;left:300px;top:34px;width:160px;border-collapse:collapse;background:var(--paper);font-size:15px;text-align:center}
  .hours th{background:var(--green-deep);color:var(--paper);font-weight:700;padding:5px 0}
  .hours td{padding:8px 0;color:var(--ink)}
  .fb{position:absolute;left:40px;top:190px;color:var(--paper);font-size:16px;font-weight:700;line-height:1.5}
  .address{position:absolute;left:40px;top:260px;color:var(--paper);font-size:19px;font-weight:700;line-height:1.6}
  .address .tel{font-size:26px}
  .map{position:absolute;left:500px;top:26px;width:360px;height:318px;background:linear-gradient(135deg,#f4f8ee,#dcebc8);border-radius:4px}
</style>
</head>
<body>
<main class="flyer">
  <div class="pattern-top" role="img" aria-label="小さなクローバーを散らした模様"></div>
  <p class="tagline">香り豊かな20種類のフレーバーティーとケーキのカフェ</p>

  <h1 class="brand"><span class="small">Sweets&amp;Cafe</span><span class="large">こもれび</span></h1>

  <svg class="ribbon" viewBox="0 0 885 180" aria-hidden="true">
    <polygon points="10,50 90,50 90,160 10,160 40,105" fill="var(--blue-deep)"/>
    <polygon points="875,50 795,50 795,160 875,160 845,105" fill="var(--blue-deep)"/>
    <path d="M60,24 Q442,-8 825,24 L825,150 Q442,118 60,150 Z" fill="var(--blue)"/>
    <ellipse cx="738" cy="96" rx="82" ry="52" fill="var(--paper)"/>
  </svg>
  <div class="ribbon-title">Grand Open!</div>
  <div class="ribbon-date">5/29</div>

  <div class="side-leaf left" role="img" aria-label="クローバーの飾り"></div>
  <div class="side-leaf right" role="img" aria-label="クローバーの飾り"></div>
  <p class="lead"><span class="line1">4日間限定！ご来店いただいた方に</span><span class="line2">スイーツプレゼント！</span></p>

  <section class="offer left">
    <div class="offer-date">5/29<span class="dow">(木)</span>・5/30<span class="dow">(金)</span></div>
    <div class="offer-box">プチシュー</div>
  </section>

  <div class="limit-badge"><span class="s">各日</span><span class="s">限定</span><span class="n">50<small>個</small></span></div>

  <section class="offer right">
    <div class="offer-date">5/31<span class="dow">(土)</span>・6/1<span class="dow">(日)</span></div>
    <div class="offer-box">いちごミルクプリン</div>
  </section>

  <div class="pattern-bottom" role="img" aria-label="小さなクローバーを並べた模様"></div>

  <footer class="footer">
    <div class="footer-brand"><span class="small">Sweets&amp;Cafe</span><span class="large">こもれび</span></div>
    <table class="hours">
      <tr><th>営業時間</th></tr>
      <tr><td>10:00〜19:00</td></tr>
      <tr><th>定休日</th></tr>
      <tr><td>火曜日</td></tr>
    </table>
    <p class="fb">Facebookページ有ります♪<br>https://www.facebook.com/komorebi.numata</p>
    <p class="address">〒371-0815 群馬県沼田市栄和町2871-5<br><span class="tel">TEL&amp;FAX：0278-61-7350</span></p>
    <div class="map" role="img" aria-label="店舗周辺の案内地図（駐車場あり）"></div>
  </footer>
</main>
</body>
</html>
```